Flalzflyer-Design (Folder)
Da für uns neben einem guten Design ein angenehmer und konstruktiver Dialog sowie Verlässlichkeit von hoher Bedeutung ist, sind wir sehr froh auf dieser Plattform auf "brightpixel" gestoßen zu sein. Wir sagen ganz herzlich DANKE!!
Zielgruppe
Zielgruppe im Bereich der Vermietung sind Alleinreisende oder als Paar verreisende Natur- und Nordsee verbundene Feriengäste (ü30) mit dem Urlaubsziel 'Sylt', welche eine persönlich und mit besonderem Schick eingerichtet Ferienwohnung/Ferienapartment in zentraler Lage in Westerland suchen und die es als positiven bzw. interessanten Aspekt sehen, dass die Ferienwohnungen direkt von uns Insulaner angeboten werden und wir als Sylter Familie ebenfalls Vor-Ort mit dem Urlaubern unter dem selben Dach leben (wenn auch nicht in der derselben Wohnung ;) ), ganz gemäß unserem Slogan 'Küstenferien Tür an Tür mit Gastgebern'
Aufgabenstellung
Es soll ein Falzflyer (Folder) mit Wickelfalz (siehe ggf. https://www.druckhafen-muster.de/werbemittel/folder.html) designed werden (4/4-farbig Euroskala). Bestehend aus einem Papier Format DIN A4 mit zwei Falzen, sodass sich bei Berücksichtigung von Vor- u. Rückseite 6 Seiten ergeben. Die wesentlichen Texte/Inhalte/Informationen, finden sich hier: https://www.urlaubsquartier-beispiel.de/481527/ . Neben dem Ferienapartment 'Möwe' w ird von uns die Ferienwohnung 'Brolke' (friesisch für Seestern) angeboten, ebenfalls im Dünenhain Quartier HOUSE (EST. 2017).
Preisangaben können unberücksichtigt beliben, da sie dem Folder später über eine gesondere Einlage beigelegt werden sollen.
Im Rahmen des Dateiupload bei entwurfsportal werden nur einige der möglichen Fotos bereitgestellt. Sie sollen als Auswahlmöglichkeit dienen. Welche der Fotos Verwendung finden oder nach weiteren nachgefragt wird, soll in Abhängigkeit mit dem Gesamtdesign stehen und zunächst von Ihnen entschieden werden, um ein möglichst ansprechenden und harmonischen Folder kreieren zu können.

```html
<!DOCTYPE html>
<html lang="de">
<head>
<meta charset="utf-8">
<title>Falzflyer Dünenhain Quartier House</title>
<link href="https://fonts.googleapis.com/css2?family=Source+Sans+3:wght@400;600;700&family=Allura&display=swap" rel="stylesheet">
<style>
:root{
  --stage:#b4b4b4;
  --paper:#ffffff;
  --fold:#3a3a3a;
  --box:#d0c8bf;
  --ink-light:#ffffff;
  --ink-dark:#6e6055;
  --heading:#7d6d61;
  --brand:#2d2d2d;
}
*{box-sizing:border-box;margin:0;padding:0}
html,body{width:839px;height:1200px;overflow:hidden;background:var(--stage)}
body{position:relative;font-family:"Source Sans 3",Arial,sans-serif}
.sheet{position:absolute;left:50px;width:738px;height:515px;background:var(--paper);border:1px solid var(--fold);box-shadow:6px 8px 14px rgba(0,0,0,.25);display:flex}
.sheet--outside{top:49px}
.sheet--inside{top:643px}
.panel{position:relative;width:246px;height:100%;border-right:1px solid var(--fold);overflow:hidden}
.panel:last-child{border-right:none}
.photo{position:absolute;display:block}
.panel-photo{left:0;top:0;width:100%;height:123px}
.box{position:absolute;left:12px;right:12px;top:135px;bottom:12px;background:var(--box);overflow:hidden}
.box--full{top:12px}
.panorama{position:absolute;left:0;top:0;width:100%;height:123px;z-index:0;
  background:linear-gradient(180deg,#c9d6df 0%,#9fb4c3 22%,#6f8ea4 40%,#c7bba5 55%,#b9a98e 70%,#a59a62 100%)}
.sheet--inside .panel{z-index:1;overflow:visible}
.dots{position:absolute;left:12px;right:8px;border-top:1.5px dotted var(--ink-light)}
.label{font-weight:700;font-size:8px;letter-spacing:.09em;text-transform:uppercase;color:var(--ink-light)}
.label--dark{color:var(--heading);font-size:6.6px}
.script{font-family:"Allura",cursive;color:var(--heading);font-weight:400;line-height:1}
.copy{font-size:7.9px;line-height:12.9px;color:var(--ink-light)}
.copy--dark{color:var(--ink-dark)}
.abs{position:absolute}
.section{position:absolute;left:12px;right:10px}
.section .label{display:block;margin-bottom:9px}
.section .copy{margin-top:5px}
.brand-name{position:absolute;left:0;right:0;top:78px;text-align:center;font-weight:700;font-size:7px;letter-spacing:.03em;color:var(--brand)}
.gallery{position:absolute;left:28px;top:137px;display:grid;grid-template-columns:80px 80px;gap:6px}
.gallery .photo{position:static;width:80px;height:79px}
.welcome{position:absolute;left:14px;top:322px;color:var(--ink-light);font-family:"Allura",cursive;font-size:30px;line-height:1.05}
.welcome span{display:block}
.strip{position:absolute;left:12px;top:19px;display:flex;gap:4px}
.strip .photo{position:static;width:65px;height:66px}
</style>
</head>
<body>

<section class="sheet sheet--outside" aria-label="Außenseite">
  <div class="panel">
    <div class="photo panel-photo" role="img" aria-label="Foto: Rettungsturm und Strandkörbe am Strand" style="background:linear-gradient(180deg,#7f9db5 0%,#a9b9c4 35%,#ddd3c2 60%,#e6dccb 100%)"></div>
    <div class="box">
      <span class="label abs" style="left:11px;top:27px;font-size:8.6px">Ferienwohnung</span>
      <span class="script abs" style="left:100px;top:14px;font-size:40px">Brolke</span>
      <div class="dots" style="top:55px"></div>
      <div class="photo" role="img" aria-label="Foto: Schlafzimmer der Ferienwohnung mit Bett und Fenster" style="left:11px;top:72px;width:83px;height:83px;background:linear-gradient(160deg,#6a625c,#cfc6bc 50%,#9b7d70)"></div>
      <p class="copy abs" style="left:104px;top:70px;right:8px">Cuscil illautentis veris magnis as expliquam aut mo eniet, cones ulpa es corruptiam, abo. Et moluptat iliquatur alisi nobis atiisque pa doluptionsed earum, optatiorem ut iumquiae.</p>
      <span class="label label--dark abs" style="left:13px;top:189px">Grundriss Ferienwohnung Brolke</span>
      <div class="photo" role="img" aria-label="Grundriss der Ferienwohnung" style="left:12px;top:213px;width:186px;height:118px;background:linear-gradient(90deg,#f4f1dc 0%,#f1efdc 70%,#d6e9f7 100%)"></div>
    </div>
  </div>

  <div class="panel">
    <div class="photo panel-photo" role="img" aria-label="Foto: in den Sand geschriebener Inselname" style="background:linear-gradient(180deg,#a9a39a,#c5bfb5 50%,#b3ada4)"></div>
    <div class="box">
      <div class="section" style="top:21px">
        <span class="label">Lage</span>
        <p class="copy">Cuscil illautentis veris magnis as expliquam aut mo eniet, cones ulpa es corruptiam, abo.<br>Et moluptat iliquatur alisi nobis atiisque pa doluptionsed earum, optatiorem ut iumquiae. Ga. Gent omni doluptatur aut que nectiae corum re aut pero .</p>
      </div>
      <div class="dots" style="top:35px"></div>
      <div class="section" style="top:128px">
        <span class="label">Anfahrt</span>
        <p class="copy">Cuscil illautentis veris magnis as expliquam aut mo eniet, cones ulpa es corruptiam, abo.<br>Et moluptat iliquatur alisi nobis atiisque pa doluptionsed earum, optatiorem ut iumquiae. Ga. Gent omni doluptatur aut que nectiae corum re aut pero .</p>
      </div>
      <div class="dots" style="top:142px"></div>
      <div class="section" style="top:230px">
        <span class="label">Kontakt</span>
        <p class="copy">Dünenhain Quartier HOUSE (EST. 2017)<br>Familie Dünenhain<br>Strandweg xxx<br>Sylt<br>Telefon 0461 55 20 38<br>e-Mail: kontakt@duenenhain-quartier.de</p>
      </div>
      <div class="dots" style="top:244px"></div>
    </div>
  </div>

  <div class="panel">
    <div class="box box--full">
      <p class="brand-name">DÜNENHAIN QUARTIER HOUSE</p>
      <div class="gallery">
        <div class="photo" role="img" aria-label="Foto: Wohnzimmer mit Sofa und Kissen" style="background:linear-gradient(160deg,#d8d2c8,#4b4a52 60%,#8fa6b3)"></div>
        <div class="photo" role="img" aria-label="Foto: Holzregal mit Dekoration" style="background:linear-gradient(160deg,#c8c2b8,#8a5a2e 55%,#c2485e)"></div>
        <div class="photo" role="img" aria-label="Foto: Strand mit Spaziergängern unter Wolkenhimmel" style="background:linear-gradient(180deg,#5f7fa3,#c7d2dc 45%,#b7aa93 70%,#d9cfbf)"></div>
        <div class="photo" role="img" aria-label="Foto: Schlafzimmer mit Einzelbett und Nachttisch" style="background:linear-gradient(160deg,#a9a198,#dad3ca 50%,#6d4d38)"></div>
      </div>
      <p class="welcome"><span>Herzlich</span><span style="padding-left:48px">Willkommen!</span></p>
    </div>
  </div>
</section>

<section class="sheet sheet--inside" aria-label="Innenseite">
  <div class="panorama" role="img" aria-label="Panoramafoto: Meer, Sandstrand und Dünen mit Strandgras"></div>

  <div class="panel">
    <div class="box">
      <span class="script abs" style="left:12px;top:18px;font-size:42px">Ferien</span>
      <span class="label abs" style="left:106px;top:18px;line-height:16px">Tür an Tür<br>mit Gastgebern</span>
      <div class="dots" style="top:55px"></div>
      <div class="photo" role="img" aria-label="Foto: Außenansicht des Ferienhauses" style="left:12px;top:69px;width:83px;height:82px;background:linear-gradient(180deg,#2f5fa8 0%,#4f7fc0 40%,#e8e2d6 55%,#6a6a5a 100%)"></div>
      <p class="copy abs" style="left:104px;top:66px;right:10px">Tio iurem quia susam, qui comnis rescimendi sinullore denis ullaborerume illuptatur alistiatur molor antinverspe pos aut quam, sum reptat.</p>
      <p class="copy copy--dark abs" style="left:12px;right:12px;top:180px">Untia porerch illuptam eos maio. Is ad moluptatur rem arupta dolent. Tio iurem quia susam, qui comnis rescimendi sinullore denis ullaborerume illuptatur alistiatur molor antinverspe pos aut quam, sum reptat dis qui officip itaquibus que por aut et vernatis ne perrovid quodipsam quaerae. Porpos pero bla corumquia consequi te volorep tiumetur maio. Cipsandant.<br>Icil este et, nonseque solent, am imagnisti tem autempor animporem quia volessitem num nis a proviti doluptae plaudignimi, sunt adio tem nulpa aut est ommos derios.</p>
    </div>
  </div>

  <div class="panel">
    <div class="box" style="overflow:visible">
      <span class="label abs" style="left:12px;top:25px">Apartment</span>
      <span class="script abs" style="left:68px;top:12px;font-size:42px">Möwe</span>
      <div class="dots" style="top:55px;right:-12px"></div>
      <div class="photo" role="img" aria-label="Foto: Wohnbereich mit Sofa, Kissen und Beistelltisch" style="left:12px;top:69px;width:209px;height:133px;background:linear-gradient(150deg,#e2ddd6 0%,#cfc8bd 35%,#3f3d44 60%,#6b6760 100%)"></div>
      <p class="copy abs" style="left:12px;right:8px;top:213px">Wer Meer hat, braucht weniger, sagt man.<br>Wir haben im Dünenhain Quartier House (est. 2017) dennoch im Vergleich zu vielen Apartments auf der Insel Sylt ein angenehmes „Mehr“ für einen schönen Aufenthalt:<br>Die Zimmer persönlich und mit Geschick gestaltet, zeitgemäße Wohneinrichtung, modernes ebenerdiges Duschbad, hochwertige Pantryküche, Smart-TV, Wlan, ansprechendes und vollständiges Geschirr, Außenbereich sowie der persönlichen Nähe zu uns Insulanern.</p>
    </div>
  </div>

  <div class="panel">
    <div class="box">
      <div class="strip">
        <div class="photo" role="img" aria-label="Foto: Schlafzimmer mit Einzelbett" style="background:linear-gradient(160deg,#a9a198,#dad3ca 50%,#6d4d38)"></div>
        <div class="photo" role="img" aria-label="Foto: Holzregal mit Dekoration" style="background:linear-gradient(160deg,#c8c2b8,#8a5a2e 55%,#c2485e)"></div>
        <div class="photo" role="img" aria-label="Foto: Duschbad mit Waschbecken" style="background:linear-gradient(160deg,#e7e4dc,#b9b4aa 50%,#9ccc3a)"></div>
      </div>
      <p class="copy abs" style="left:12px;right:8px;top:94px">Das Apartmant eignet sich für einen längeren Urlaub besonders für 1 Person. Es steht ein Einzelbett im kleinen Schlafzimmer zur Verfügung. Für einen Aufenthalt von einigen Tagen haben 2 Personen ebenfalls eine passend schöne Unterkunft (Schlafmöglichkeit auf komfortablen Schlafsofa mit Lattenrost).</p>
      <span class="label label--dark abs" style="left:12px;top:200px">Grundriss Apart. Möwe</span>
      <div class="photo" role="img" aria-label="Grundriss des Apartments" style="left:12px;top:215px;width:200px;height:134px;background:linear-gradient(90deg,#f4f1dc 0%,#f1efdc 70%,#d6e9f7 100%)"></div>
    </div>
  </div>
</section>

</body>
</html>
```